Business card design based on existing website

Please make a business card that is consistent with the look and feel of my new website: http://tellbury.com.sg. By going to the site, I think you'll have all you need in terms of the work I do and the colors I use.

I would like to ask the winner of this project to then do a separate project to design my stationery.

Target Market(s)

Heads of human resources, people wanting psychotherapy, and executives wanting coaching. (It's quite a mix!)

Industry/Entity Type

Psychology

Contact Information for Business Card

Email: ray5678@tellbury.com.sg
Website: http://tellbury.com.sg
Tel: +65 94706218

(I will not have a physical address on the card)

Font styles to use
Serif

Colors

Designer to choose colors to be used in the design.

Requirements
Must have
• On the Front
• ==========
• Have "Dr. Raymond Tellbury" using the font of the website.
• Also "Executive Coach, Psychotherapist, Leadership Professor"
• The back should mention
• ==================
• My degrees
• -------------
• "PhD Kelworth; Post Doc Drayfield". E.g., "Raymond Tellbury (PhD Kelworth; Post Doc Drayfield)" where the text between brackets was in smaller font.
• My work
• ----------
• "Executive coach, psychotherapist, and leadership professor"
• My job titles
• ---------------
• "Principal (Tellbury Consulting)
• Adjunct Professor (Lornvale Commerce University)
• Adjunct Associate Professor (Pemberly Institute of Letters)
• Coach & Supervisor (OKTRAV) '
• Options:
• 1) you can abbreviate Adjunct Professor to "Adj Prof" or "Adj Professor"; and "Adjunct Associate Professor" to "Adj Assoc Prof"
• 2) you abbreviate "Pemberly Institute of Letters" and "Lornvale Commerce University" to "PIL" and "LCU"
• 3) You can also combine the titles for PIL and LCU, e.g., "Adjunct faculty (PIL & LCU)
Nice to have
• Because I work with many Chinese people, it is sometimes helpful to have my family name, "Tellbury", in caps. In the past I have not used caps because it takes away from the aesthetic of the card. Only use caps if it looks good.
• The uploaded image of a "RT" is something that may be helpful. I am undecided.
• THANK YOU for helping me!
Should not have
• No photos. In my industry people consider it overselling.

```html
<!DOCTYPE html>
<html lang="en">
<head>
<meta charset="utf-8">
<title>Dr. Raymond Tellbury – Business Card</title>
<link rel="stylesheet" href="https://fonts.googleapis.com/css2?family=Crimson+Pro:wght@400;700&display=swap">
<style>
  :root {
    --page-bg: #e6e8e7;
    --card-white: #fbfbfb;
    --slate: #3a4a4d;
    --name-ink: #1e2b23;
    --heading-ink: #2a352f;
    --body-ink: #5a5f5c;
    --rule: #8a908d;
    --light-ink: #f4f4f2;
    --serif: "Crimson Pro", "Palatino Linotype", Georgia, serif;
  }
  * { margin: 0; padding: 0; box-sizing: border-box; }
  html, body {
    width: 1200px; height: 1134px; overflow: hidden;
    background: var(--page-bg);
    font-family: var(--serif);
  }
  .card {
    position: absolute;
    left: 261px;
    width: 675px;
    height: 381px;
    border-radius: 14px;
    overflow: hidden;
    box-shadow: 0 4px 14px rgba(0,0,0,0.18);
  }
  .card--front { top: 161px; background: var(--card-white); }
  .card--back { top: 590px; background: var(--slate); }

  .front__band {
    position: absolute; left: 0; right: 0; bottom: 0; height: 19px;
    background: var(--slate);
  }
  .abs { position: absolute; white-space: nowrap; line-height: 1; }

  .holder-name {
    left: 38px; top: 62px;
    font-size: 30px; font-weight: 700; color: var(--name-ink);
    letter-spacing: 0.2px;
  }
  .titles { left: 38px; top: 103px; color: var(--body-ink); font-size: 16px; line-height: 19.3px; }
  .section-rule { position: absolute; left: 38px; height: 1.5px; background: var(--rule); }
  .section-rule--degrees { top: 189px; width: 110px; }
  .section-rule--work { top: 264px; width: 86px; }
  .section-heading { left: 38px; font-size: 22px; font-weight: 400; color: var(--heading-ink); }
  .section-heading--degrees { top: 201px; }
  .section-heading--work { top: 279px; }
  .section-body { left: 38px; font-size: 16px; line-height: 19.3px; color: var(--body-ink); }
  .section-body--degrees { top: 229px; }
  .section-body--work { top: 306px; }

  .contact {
    position: absolute; right: 42px; top: 272px;
    display: flex; flex-direction: column; align-items: flex-end; gap: 6px;
    font-size: 16px; font-style: normal; color: var(--body-ink);
  }
  .contact__row { display: flex; align-items: center; gap: 7px; line-height: 18px; }
  .contact__icon { width: 15px; height: 15px; fill: var(--slate); }

  .brand-name { font-family: var(--serif); font-weight: 400; line-height: 1; }
  .brand-name--front {
    right: 42px; top: 100px;
    font-size: 54px; color: var(--slate);
  }
  .brand-name--back {
    left: 0; right: 0; top: 122px; text-align: center;
    font-size: 72px; color: var(--light-ink);
  }
  .back-url {
    left: 0; right: 0; top: 326px; text-align: center;
    font-size: 16px; color: var(--light-ink);
  }
</style>
</head>
<body>
  <section class="card card--front" aria-label="Card front">
    <h1 class="abs holder-name">Dr. Raymond Tellbury</h1>
    <p class="abs titles">Principal (Tellbury Consulting)<br>Adjunct Professor (LCU)<br>Adjunct Associate Professor (PIL)<br>Coach &amp; Supervisor (OKTRAV)</p>

    <div class="section-rule section-rule--degrees"></div>
    <h2 class="abs section-heading section-heading--degrees">My degrees</h2>
    <p class="abs section-body section-body--degrees">PhD Kelworth; Post Doc Drayfield</p>

    <div class="section-rule section-rule--work"></div>
    <h2 class="abs section-heading section-heading--work">My work</h2>
    <p class="abs section-body section-body--work">Executive coach, psychotherapist<br>and leadership trainer</p>

    <div class="abs brand-name brand-name--front">Tellbury</div>

    <address class="contact">
      <div class="contact__row">+65 94706218
        <svg class="contact__icon" viewBox="0 0 16 16" aria-hidden="true"><path d="M2 6c0-2 2.5-3.5 6-3.5S14 4 14 6v1h-3V5.5H5V7H2z"/><path d="M4 8h8l1.5 5.5h-11z"/></svg>
      </div>
      <div class="contact__row">ray5678@tellbury.com.sg
        <svg class="contact__icon" viewBox="0 0 16 16" aria-hidden="true"><path d="M1 3.5h14v9H1z"/><path d="M1.5 4l6.5 5 6.5-5" fill="none" stroke="#fbfbfb" stroke-width="1.2"/></svg>
      </div>
      <div class="contact__row">www.tellbury.com.sg
        <svg class="contact__icon" viewBox="0 0 16 16" aria-hidden="true"><circle cx="8" cy="8" r="7"/><g fill="none" stroke="#fbfbfb" stroke-width="1"><ellipse cx="8" cy="8" rx="3" ry="6.5"/><path d="M1.5 8h13M2.5 5h11M2.5 11h11"/></g></svg>
      </div>
    </address>

    <div class="front__band"></div>
  </section>

  <section class="card card--back" aria-label="Card back">
    <div class="abs brand-name brand-name--back">Tellbury</div>
    <p class="abs back-url">www.tellbury.com.sg</p>
  </section>
</body>
</html>
```